Give us a remarkable appearance

We need a unique, remarkable stationery design (Business Cards, Business Letters, Email Signature etc.). The design should use our logo.

Veltro-Consulting is a startup in consulting, management and IT services and individual software development for the financial industry.

Veltro in english is agate stone. We would like to see designs that use colors out of the agate stone color range.

Preferred COLORS: gold, dark red (burgundy), white, dark grey, black ** see attached Logos **

The used font should be available for further usage with texts etc.

The design should express: modernity, precious, high quality, lightness, stability, ecological awareness, speedy, reliability, simplicity, sustainability.

Target Market(s)

C-Level and Business Clients, Professionals

Industry/Entity Type

Business

Logo Text

Logo styles of interest
Pictorial/Combination Logo
Abstract Logo
Wordmark Logo
Requirements
Must have
• Business Cards, Business Papers, Email Signature
Nice to have
• Door plate, Flyersheet (basic structure), Envelop...

```html
<!DOCTYPE html>
<html lang="en">
<head>
<meta charset="utf-8">
<title>Veltro Consulting – Stationery</title>
<link rel="stylesheet" href="https://fonts.googleapis.com/css2?family=Michroma&display=swap">
<style>
  :root{
    --brand-red:#be1e2d;
    --band-soft:#e9a08f;
    --paper:#ffffff;
    --stage:#e4e5e7;
    --stage-light:#f2f3f4;
    --shadow:rgba(0,0,0,.35);
  }
  *{box-sizing:border-box;margin:0;padding:0}
  html,body{width:1200px;height:960px;overflow:hidden}
  body{
    background:radial-gradient(ellipse at 50% 45%,var(--stage-light),var(--stage) 70%);
    font-family:"Michroma",sans-serif;
    position:relative;
  }
  span{line-height:1}
  .sheet{position:absolute;background:var(--paper);box-shadow:2px 3px 8px var(--shadow);overflow:hidden}
  .sheet svg.band{position:absolute;left:0;top:0;width:100%;height:100%}
  .brand-name{color:var(--paper);white-space:nowrap;position:absolute;letter-spacing:.04em}
  .label{position:absolute;color:var(--paper);font-size:7.5px;letter-spacing:.08em;white-space:nowrap;text-align:right}
  .label.red{color:var(--brand-red)}
  .web{position:absolute;color:var(--brand-red);font-size:8px;white-space:nowrap}

  /* letterhead */
  .letterhead{left:38px;top:40px;width:476px;height:673px}
  .letterhead .header{position:absolute;left:0;top:0;width:100%;height:62px;background:var(--brand-red)}
  .letterhead .rule{position:absolute;left:0;top:62px;width:100%;height:4px;background:linear-gradient(90deg,#f3c9bf,var(--band-soft) 50%,#f3c9bf)}

  /* cover sheet */
  .cover{left:691px;top:18px;width:476px;height:673px;background:var(--brand-red)}
  .cover .brand-name{left:200px;top:586px;font-size:22px}
  .cover .web{left:107px;top:654px;color:var(--paper);font-size:15px}

  /* large envelope */
  .envelope{left:378px;top:227px;width:609px;height:335px}
  .envelope .foot-rule{position:absolute;left:6px;top:304px;width:597px;height:2px;background:linear-gradient(90deg,#f6d6cf,var(--brand-red) 60%,#f6d6cf)}

  /* business cards */
  .card{top:774px;width:201px;height:114px}
  .card-front{left:68px}
  .card-back{left:285px}
  .card-front .top{position:absolute;left:0;top:0;width:100%;height:46px;background:var(--brand-red)}
  .card-back .bottom{position:absolute;left:0;top:46px;width:100%;height:68px;background:var(--brand-red)}
  .card .person{position:absolute;left:10px;top:56px;color:var(--brand-red);font-size:7px}
  .card .role{position:absolute;left:31px;top:66px;color:var(--brand-red);font-size:4.5px}
  .card .contact{position:absolute;left:10px;color:#444;font-size:4px}
  .card .line{position:absolute;left:0;height:1px;background:var(--brand-red)}

  /* DL envelope */
  .dl{left:621px;top:709px;width:511px;height:223px}
  .dl .header{position:absolute;left:0;top:0;width:100%;height:67px;background:var(--brand-red)}
  .dl .rule{position:absolute;left:0;top:67px;width:100%;height:4px;background:linear-gradient(90deg,#f3c9bf,var(--band-soft) 50%,#f3c9bf)}
  .dl .window{position:absolute;left:320px;top:141px;width:162px;height:65px;border-radius:33px;border:1px solid #bbb;background:var(--paper);box-shadow:inset 0 0 4px rgba(0,0,0,.15)}
</style>
</head>
<body>
<svg width="0" height="0" style="position:absolute">
  <defs>
    <linearGradient id="ribbon" x1="0" x2="1">
      <stop offset="0" stop-color="#be1e2d" stop-opacity=".9"/>
      <stop offset=".5" stop-color="#e9a08f" stop-opacity=".7"/>
      <stop offset="1" stop-color="#f3c0b3" stop-opacity=".5"/>
    </linearGradient>
    <linearGradient id="ribbon-light" x1="0" x2="1">
      <stop offset="0" stop-color="#ffffff" stop-opacity=".05"/>
      <stop offset="1" stop-color="#ffffff" stop-opacity=".35"/>
    </linearGradient>
  </defs>
</svg>

<!-- Letterhead -->
<section class="sheet letterhead">
  <div class="header"></div>
  <div class="rule"></div>
  <span class="brand-name" style="left:14px;top:26px;font-size:14px">VELTRO CONSULTING</span>
  <span class="label" style="right:88px;top:7px">Address:</span>
  <span class="label" style="right:88px;top:43px">Phone:</span>
  <span class="label" style="right:88px;top:53px">Mail:</span>
  <svg class="band" viewBox="0 0 476 673" role="img" aria-label="Flowing ribbon of fine red lines">
    <path d="M0,673 C120,640 250,650 330,620 C400,595 400,560 430,545 C450,535 465,530 476,528 L476,548 C455,555 440,570 430,590 C410,630 330,655 200,665 C120,670 60,672 0,673Z" fill="url(#ribbon)"/>
  </svg>
  <span class="web" style="right:4px;bottom:5px">www.veltroconsulting.com</span>
</section>

<!-- Cover sheet -->
<section class="sheet cover">
  <svg class="band" viewBox="0 0 476 673" role="img" aria-label="Fine white line ribbons sweeping across the sheet">
    <path d="M476,260 C400,265 330,290 300,330 L300,345 C340,305 400,285 476,290Z" fill="url(#ribbon-light)"/>
    <path d="M300,450 C330,520 380,590 476,665 L460,673 C370,600 320,530 300,470Z" fill="url(#ribbon-light)"/>
    <path d="M0,665 C60,630 110,590 150,540 L160,550 C120,600 70,640 10,673Z" fill="url(#ribbon-light)"/>
  </svg>
  <span class="brand-name">VELTRO</span>
  <span class="brand-name" style="left:200px;top:616px;font-size:10px;letter-spacing:.3em">CONSULTING</span>
  <span class="web">www.veltroconsulting.com</span>
</section>

<!-- Large envelope -->
<section class="sheet envelope">
  <svg class="band" viewBox="0 0 609 335" role="img" aria-label="Red corner with flowing ribbon of fine lines">
    <path d="M0,0 H609 V4 C430,18 250,10 120,32 C90,40 85,95 0,110Z" fill="var(--brand-red)"/>
    <path d="M0,110 C85,95 90,40 120,32 C250,10 430,18 609,4 L609,10 C450,28 270,22 125,42 C100,50 95,115 0,165Z" fill="url(#ribbon)" opacity=".75"/>
  </svg>
  <span class="brand-name" style="left:10px;top:34px;font-size:11px">VELTRO</span>
  <div class="foot-rule"></div>
  <span class="label red" style="left:8px;top:312px">Address:</span>
  <span class="label red" style="right:129px;top:312px">Phone:</span>
  <span class="label red" style="right:129px;top:322px">Mail:</span>
</section>

<!-- Business card front -->
<section class="sheet card card-front">
  <div class="top"></div>
  <span class="brand-name" style="left:8px;top:20px;font-size:10px">VELTRO</span>
  <div class="line" style="top:54px;width:100px"></div>
  <span class="person">NAME SURNAME</span>
  <div class="line" style="top:65px;width:124px"></div>
  <span class="role">POSITION</span>
  <span class="contact" style="top:78px">&#9742; +12 555010200</span>
  <span class="contact" style="top:85px">&#9993; office@veltroconsulting.com</span>
  <svg class="band" viewBox="0 0 201 114" role="img" aria-label="Ribbon of fine red lines">
    <path d="M0,112 C60,100 150,108 175,80 C185,65 190,50 201,45 L201,58 C193,65 188,85 178,95 C150,112 70,112 0,114Z" fill="url(#ribbon)"/>
  </svg>
</section>

<!-- Business card back -->
<section class="sheet card card-back">
  <div class="bottom"></div>
  <svg class="band" viewBox="0 0 201 114" role="img" aria-label="Ribbon of fine red lines">
    <path d="M0,46 C15,35 20,15 40,10 C90,5 150,8 201,0 L201,4 C150,12 95,14 48,20 C28,25 25,50 10,56Z" fill="url(#ribbon)"/>
  </svg>
  <span class="web" style="left:59px;top:30px;font-size:6.5px">www.veltroconsulting.com</span>
  <span class="brand-name" style="left:56px;top:72px;font-size:18px">VELTRO</span>
</section>

<!-- DL envelope -->
<section class="sheet dl">
  <div class="header"></div>
  <div class="rule"></div>
  <span class="brand-name" style="left:14px;top:28px;font-size:14px">VELTRO CONSULTING</span>
  <span class="label" style="right:104px;top:8px">Address:</span>
  <span class="label" style="right:104px;top:44px">Phone:</span>
  <span class="label" style="right:104px;top:54px">Mail:</span>
  <svg class="band" viewBox="0 0 511 223" role="img" aria-label="Flowing ribbon of fine red lines">
    <path d="M0,223 C120,200 250,205 330,195 C420,185 430,120 450,105 C470,95 490,88 511,84 L511,100 C490,105 475,115 465,140 C440,195 380,205 300,212 C200,218 100,220 0,223Z" fill="url(#ribbon)"/>
  </svg>
  <div class="window"></div>
  <span class="web" style="right:6px;bottom:6px">www.veltroconsulting.com</span>
</section>
</body>
</html>
```